Landing page для Vamlor parts
Название сайта (домена, или проекта)
Vamlor parts
Выберите сайты-победители прошлых конкурсов, чтобы дизайнерам был понятен нужный вам стиль
Укажите ссылки на сайты, которые нравятся
https://tridovka.ru/
Оптово-розничные покупатели оригинальных запчастей на автомобили. Средний чек от 30 000 рублей. Мужчины. Мы возим только оригинальные запчасти из Европы, у нас высокая скорость доставки! от 5 рабочих дней.
Этот сайт в принципе нравится https://palmesto.ru/?ysclid=qwert7xz2b814263590 ( не сама цветовая гамма) а расположение блоков.
У нас сайт создан на платформе KRUM. Платформа предполагает использование шаблонных вариантов сайта, то есть сайт реализован на готовом шаблоне. Ниже мы прикладываем используемый шаблон.
https://vamlor-parts.ru/?templateId=31&class=301&color=206351
Важно учитывать, что выход за рамки возможностей шаблона невозможен. Поэтому макет дизайна лендинг-пейджа по техническому заданию, представленному ниже, необходимо разрабатывать строго с учётом функциональных и визуальных возможностей, которые предоставляет данный шаблон сайта.
https://docs.example-files.net/document/d/7Kd_prTq2mXz9WbLe4HnRs0VyUj3cAoF8QgtZ1NxYbPw/edit?tab=t.0
Адаптивность сайта
Десктопная версия, Версия для планшетов, Версия для телефонов

```html
<!DOCTYPE html>
<html lang="ru">
<head>
<meta charset="utf-8">
<title>Vamlor parts — оригинальные автозапчасти из Европы</title>
<link rel="stylesheet" href="https://fonts.googleapis.com/css2?family=Oswald:wght@400;500&family=Roboto:wght@400;500&display=swap">
<style>
:root{
  --stage:#2b2b2b;
  --page:#1c1c1c;
  --card:#222;
  --line:#444;
  --text:#f2f2f2;
  --muted:#a6a6a6;
  --accent:#c8312b;
  --star:#f1b52b;
}
*{box-sizing:border-box;margin:0;padding:0}
html,body{width:1200px;height:915px;overflow:hidden;background:var(--stage);font-family:"Roboto",Arial,sans-serif;color:var(--text)}
.stage{position:relative;width:1200px;height:915px}
.h{font-family:"Oswald","Arial Narrow",sans-serif;font-weight:500;text-transform:uppercase;letter-spacing:.2px}

/* first screen */
.screen-main{position:absolute;left:0;top:0;width:660px;height:626px;background:var(--page);overflow:hidden}
.hero{position:absolute;left:0;top:0;width:660px;height:225px;background:radial-gradient(ellipse at 75% 30%,#3a3a3a 0%,#242424 45%,#1c1c1c 80%)}
.hero-title{position:absolute;left:60px;top:-16px;font-size:29px;line-height:40px}
.hero-tags{position:absolute;left:60px;top:90px;display:flex;gap:22px;font-size:10px;color:#ddd;font-family:"Oswald",sans-serif;text-transform:uppercase}
.btn{position:absolute;top:144px;height:30px;display:flex;align-items:center;justify-content:center;font-size:8px;border-radius:2px}
.btn-primary{left:48px;width:90px;background:var(--accent)}
.btn-ghost{left:156px;width:104px;border:1px solid #bbb}
.makers-title{position:absolute;left:48px;top:258px;font-size:18px}
.makers{position:absolute;left:48px;top:305px;display:flex;gap:17px}
.maker{width:44px;height:44px;border-radius:50%;background:#4a4a4a}
.card{position:absolute;border:1px solid var(--line);border-radius:6px;background:var(--card);padding:12px}
.card-big{left:48px;top:411px;width:227px;height:190px}
.card-big .h{font-size:17px;line-height:20px;white-space:nowrap;letter-spacing:0}
.card-big .pic{position:absolute;left:12px;top:66px;width:90px;height:70px;border-radius:6px;background:radial-gradient(circle,#9a9a9a,#3a3a3a 70%)}
.card-big p{position:absolute;left:12px;bottom:14px;width:200px;font-size:8px;color:var(--muted);line-height:11px}
.card-s{width:133px;height:89px}
.card-s .h{font-size:22px}
.card-s p{font-size:8px;color:var(--muted);margin-top:14px;line-height:11px}

/* second screen */
.screen-info{position:absolute;left:591px;top:209px;width:609px;height:706px;background:var(--page);overflow:hidden;border-left:1px solid #333}
.screen-info .bg{position:absolute;left:0;top:0;width:609px;height:240px;background:radial-gradient(ellipse at 60% 20%,#353535,#1c1c1c 70%)}
.brand-ghost{position:absolute;left:40px;top:-14px;font-family:"Oswald",sans-serif;font-size:110px;font-weight:500;color:#fff;opacity:.07;letter-spacing:8px}
.stats{position:absolute;left:46px;top:78px;display:flex}
.stat .h{font-size:32px;font-weight:400}
.stat p{font-size:7px;color:var(--muted);line-height:9px;margin-top:6px}
.steps-title{position:absolute;left:43px;top:210px;font-size:18px}
.steps{position:absolute;left:43px;top:245px;display:flex;gap:16px}
.step{width:121px;height:91px;border:1px solid var(--line);border-radius:6px;background:rgba(34,34,34,.9);padding:8px 10px;position:relative}
.step .h{font-size:30px;font-weight:400}
.step p{position:absolute;left:10px;bottom:10px;font-size:7px;color:var(--muted)}
.quote{position:absolute;left:43px;top:394px;font-size:19px;line-height:24px}
.reviews{position:absolute;left:43px;top:459px;width:520px;height:152px;background:#2b2b2b;border-radius:4px;padding:8px 10px}
.reviews-head{display:flex;justify-content:space-between;align-items:center;font-size:7px}
.stars{color:var(--star);font-size:7px}
.review-btn{background:var(--accent);padding:3px 8px;font-size:6px;border-radius:2px}
.review-list{display:flex;gap:9px;margin-top:10px}
.review{width:117px;min-height:90px;background:#1f1f1f;border-radius:3px;padding:6px;font-size:5px;line-height:7px;color:#bbb}
.review b{color:#eee;font-weight:500}
.footer{position:absolute;left:43px;top:676px;width:540px;height:30px;background:#262626;border-radius:4px 4px 0 0;display:flex;align-items:center;gap:45px;padding-left:14px;font-size:7px}
.logo{font-family:"Oswald",sans-serif;font-size:12px;font-weight:500;letter-spacing:1px}
</style>
</head>
<body>
<div class="stage">

  <section class="screen-main">
    <div class="hero" role="img" aria-label="Тёмная фотография деталей автомобиля"></div>
    <h1 class="h hero-title">Оригинальные автозапчасти из Европы<br>с доставкой от 3 рабочих дней</h1>
    <div class="hero-tags"><span>100% оригинал</span><span>Гарантия совместимости</span><span>Без посредников</span></div>
    <a class="btn btn-primary">Подобрать запчасть</a>
    <a class="btn btn-ghost">Получить консультацию</a>

    <h2 class="h makers-title">Проверенные мировые производители</h2>
    <div class="makers">
      <span class="maker"></span><span class="maker"></span><span class="maker"></span>
      <span class="maker"></span><span class="maker"></span><span class="maker"></span>
      <span class="maker"></span><span class="maker"></span><span class="maker"></span>
    </div>

    <div class="card card-big">
      <div class="h">Надежные запчасти<br>без границ и ожиданий</div>
      <div class="pic" role="img" aria-label="Тормозной диск и суппорт"></div>
      <p>Работаем только с официальными поставщиками, без перекупщиков</p>
    </div>
    <div class="card card-s" style="left:288px;top:411px"><div class="h">100%</div><p>гарантия совместимости,<br>проверка по VIN</p></div>
    <div class="card card-s" style="left:432px;top:411px"><div class="h">3–7</div><p>рабочих дней доставка<br>в Россию</p></div>
    <div class="card card-s" style="left:288px;top:511px"><div class="h">100%</div><p>оригинальные<br>автозапчасти из Европы</p></div>
    <div class="card card-s" style="left:432px;top:511px"><div class="h">12</div><p>месяцев гарантии от<br>производителя</p></div>
  </section>

  <section class="screen-info">
    <div class="bg" role="img" aria-label="Тёмный фон с деталями двигателя"></div>
    <div class="brand-ghost">VAMLOR</div>
    <div class="stats">
      <div class="stat" style="width:78px"><div class="h">10+</div><p>лет работаем<br>для вас</p></div>
      <div class="stat" style="width:136px"><div class="h">27 000+</div><p>довольных<br>клиентов</p></div>
      <div class="stat" style="width:91px"><div class="h">80%</div><p>повторных<br>обращений</p></div>
      <div class="stat"><div class="h">2</div><p>офиса Москва<br>и Санкт-Петербург</p></div>
    </div>

    <h2 class="h steps-title">Как мы работаем</h2>
    <div class="steps">
      <div class="step"><div class="h">1</div><p>Вы оставляете заявку или VIN</p></div>
      <div class="step"><div class="h">2</div><p>Мы подбираем нужную деталь</p></div>
      <div class="step"><div class="h">3</div><p>Согласуем сроки и стоимость</p></div>
      <div class="step"><div class="h">4</div><p>Доставка и гарантия</p></div>
    </div>

    <h2 class="h quote">«Запчасти были точно те, которые я заказывала,<br>и качество соответствовало ожиданиям»</h2>

    <div class="reviews">
      <div class="reviews-head">
        <div><b>ОТЗЫВЫ НА VAMLOR PARTS</b><br><span class="stars">★★★★★</span> 4.9 / 5 (161 отзыв)</div>
        <span class="review-btn">Оставить отзыв</span>
      </div>
      <div class="review-list">
        <div class="review"><b>Артём Ланской</b> <span class="stars">★★★★★</span><br>Заказывал колодки и диски, всё пришло быстрее обещанного. Подобрали по VIN без ошибок, менеджер всегда был на связи. Буду обращаться ещё.</div>
        <div class="review"><b>Ольга Т.</b> <span class="stars">★★★★★</span><br>Запчасти были точно те, которые я заказывала, качество соответствовало ожиданиям. Спасибо за помощь и честные сроки доставки.</div>
        <div class="review"><b>Павел</b> <span class="stars">★★★★★</span><br>Хороший сервис, оригинал по адекватной цене. Всё упаковано аккуратно, документы в порядке.</div>
        <div class="review"><b>Руслан В.</b> <span class="stars">★★★★★</span><br>Работаю с ребятами давно, берём детали для сервиса. Надёжно, быстро и без лишних вопросов.</div>
      </div>
    </div>

    <footer class="footer">
      <span class="logo">VAMLOR</span>
      <span>О КОМПАНИИ</span>
      <span>ПОКУПАТЕЛЯМ</span>
      <span>КОНТАКТНЫЕ ДАННЫЕ</span>
    </footer>
  </section>

</div>
</body>
</html>
```